3D visuals for homeowners planning a building project, visuals show how house would look...

I offer excellent quality 3D visuals of how home would look after building project or renovation has been completed.
A5 double sided please,

I would not like to influence you too much but I thought that flyer could for exemple show "before...and after"
(like regrowing someone`s hair :-)))

where "before" would be a boring black/white drawing (uploaded), and "after" - the superb 3D visual etc...

front side could be this building project - kitchen extension and back side coud be bathroom,

again - its just an idea, I actually submitted the project to MakerHive as I dont trust too much my own judgment :-)

I hope someone has better idea !!!

Target Market(s)

Homeowners planning a building project

Industry/Entity Type

Graphic Art

Requirements
Must have
• I offer 3D home visuals.
• Excellent detailed quality.
• Only £32 per image.
• Tel : 07700900418
• email : quillbeam@mernova.net

```html
<!DOCTYPE html>
<html lang="en">
<head>
<meta charset="utf-8">
<title>Quillbeam – 3D Home Visuals</title>
<link rel="stylesheet" href="https://fonts.googleapis.com/css2?family=Mukta:wght@500;700;800&display=swap">
<style>
:root{
  --navy:#1f2a6b;
  --blue:#2e5fd0;
  --sky:#4aa6e2;
  --orange:#f6a12e;
  --peach:#fbd6a6;
  --lavender:#dcd8f0;
  --white:#ffffff;
  --paper:#f4f5f8;
  --line-grey:#c3c7d3;
}
*{margin:0;padding:0;box-sizing:border-box}
html,body{width:847px;height:1200px;overflow:hidden;background:var(--white)}
body{font-family:"Mukta",Arial,sans-serif;color:var(--navy)}
.flyer{position:relative;width:847px;height:1200px;overflow:hidden;background:var(--white)}
.backdrop{position:absolute;inset:0}
.brand{position:absolute;left:56px;top:30px}
.brand-name{font-size:58px;font-weight:800;line-height:1;letter-spacing:1px;color:var(--navy)}
.brand-tagline{font-size:33px;font-weight:500;color:var(--orange);margin-top:6px;line-height:1.1}
.headline{position:absolute;left:56px;top:182px;width:600px;font-size:28px;font-weight:800;line-height:1.27;color:var(--navy);text-transform:uppercase}
.headline em{font-style:normal;color:var(--blue)}
.label-before{position:absolute;left:28px;top:356px;height:40px;padding:0 14px;display:flex;align-items:center;background:var(--blue);color:var(--white);font-size:19px;font-weight:700;border-radius:3px 3px 0 0}
.visual{position:absolute}
.visual-drawing{left:28px;top:396px;width:312px;height:270px;background:linear-gradient(135deg,var(--white) 0%,var(--paper) 55%,#e4e7ee 100%);border:3px solid var(--line-grey)}
.visual-render{left:438px;top:414px;width:392px;height:322px;border:4px solid var(--orange);background:linear-gradient(180deg,#f2ece4 0%,#e3d8ca 38%,#cfc5b9 62%,#9a9692 82%,#5f6064 100%)}
.label-after{position:absolute;left:438px;top:414px;width:392px;height:38px;background:var(--orange);color:var(--white);font-size:19px;font-weight:700;display:flex;align-items:center;justify-content:center}
.arrow{position:absolute;left:230px;top:360px}
.promise{position:absolute;left:354px;top:752px;font-size:26px;font-weight:700;color:var(--blue);white-space:nowrap}
.benefits{position:absolute;left:126px;top:850px;width:440px;font-size:29px;font-weight:700;line-height:1.2;color:var(--navy)}
.price-badge{position:absolute;left:628px;top:806px;width:218px;height:218px;border-radius:50%;background:var(--white);display:flex;flex-direction:column;align-items:center;justify-content:center;text-align:center;color:var(--navy);font-weight:700;line-height:1.15}
.price-badge .small{font-size:21px}
.price-badge .price{font-size:40px;font-weight:800;line-height:1.05}
.price-badge .per{font-size:21px;margin-top:8px}
.contact{position:absolute;left:30px;top:1060px;font-size:30px;font-weight:700;font-style:normal;color:var(--blue);line-height:1.5;text-transform:uppercase}
</style>
</head>
<body>
<div class="flyer">
  <svg class="backdrop" width="847" height="1200" viewBox="0 0 847 1200" aria-hidden="true">
    <path d="M0 880 C160 830 300 770 520 762 C700 756 790 720 847 700 L847 1200 L0 1200 Z" fill="var(--lavender)"/>
    <circle cx="800" cy="30" r="30" fill="var(--navy)"/>
    <circle cx="735" cy="65" r="34" fill="var(--peach)"/>
    <circle cx="640" cy="110" r="24" fill="var(--orange)"/>
    <circle cx="700" cy="150" r="20" fill="var(--sky)"/>
    <circle cx="785" cy="130" r="42" fill="var(--navy)"/>
    <circle cx="690" cy="30" r="14" fill="var(--sky)"/>
    <circle cx="740" cy="210" r="28" fill="var(--orange)"/>
    <circle cx="820" cy="215" r="18" fill="var(--sky)"/>
    <circle cx="640" cy="200" r="14" fill="var(--navy)"/>
    <circle cx="28" cy="742" r="16" fill="var(--navy)"/>
    <circle cx="66" cy="728" r="10" fill="var(--sky)"/>
    <circle cx="76" cy="772" r="22" fill="var(--orange)"/>
    <circle cx="28" cy="812" r="26" fill="var(--peach)"/>
    <circle cx="100" cy="818" r="13" fill="var(--sky)"/>
    <circle cx="66" cy="840" r="8" fill="var(--navy)"/>
  </svg>

  <header class="brand">
    <h1 class="brand-name">QUILLBEAM</h1>
    <p class="brand-tagline">3D Home Visuals</p>
  </header>

  <h2 class="headline">Planning a <em>building project</em><br>and want to see what it<br>might look like <em>in real-life</em>?</h2>

  <span class="label-before">We turn dull 2D drawings</span>
  <div class="visual visual-drawing" role="img" aria-label="Black and white 2D floor plan drawing of a bathroom layout"></div>

  <svg class="arrow" width="220" height="80" viewBox="0 0 220 80" aria-hidden="true">
    <path d="M8 66 C60 8 140 0 192 42" fill="none" stroke="var(--sky)" stroke-width="6" stroke-linecap="round"/>
    <path d="M176 26 L204 52 L170 58 Z" fill="var(--sky)"/>
  </svg>

  <div class="visual visual-render" role="img" aria-label="Realistic 3D rendered visual of the finished bathroom with tiled walls, basin and shower"></div>
  <span class="label-after">Into realistic 3D visuals!</span>

  <p class="promise">We bring your ideas and designs to life</p>

  <p class="benefits">Excellent detailed quality<br>images for all building<br>projects, extensions, or<br>refurbishments</p>

  <div class="price-badge">
    <span class="small">EXPERT</span>
    <span class="small">BESPOKE DESIGN</span>
    <span class="price">ONLY £32</span>
    <span class="per">PER DRAWING</span>
  </div>

  <address class="contact">
    Tel: 07700 900418<br>
    Email: quillbeam@mernova.net
  </address>
</div>
</body>
</html>
```